Redesign Colorful Business Card

Please redesign the card attached. It is too busy. Please don't eliminate any of the words. The repetivite word "free" can be used less often.

Target Market(s)

College Students.

Contact Information for Business Card

The details listed in the attached image

Font styles to use
Sans Serif

Requirements
Must have
• A clear and simple presentation and must be attractive.

```html
<!DOCTYPE html>
<html lang="en">
<head>
<meta charset="utf-8">
<title>StudyBrisk Business Card</title>
<link rel="stylesheet" href="https://fonts.googleapis.com/css2?family=Montserrat:wght@600;700;800&family=Open+Sans:wght@400&display=swap">
<style>
  :root {
    --page-bg: #f4f4f4;
    --card-red: #8e1414;
    --card-red-light: #a91e1e;
    --card-red-dark: #5e0a0a;
    --benefit-green: #00f000;
    --headline-blue: #3b10e6;
    --badge-red: #ff0000;
    --badge-ring: #e7a23a;
    --frame-teal: #4fa7bd;
    --art-light: #f2f2f2;
    --art-red: #f0545a;
    --white: #ffffff;
    --url-red: #e8141c;
  }
  * { box-sizing: border-box; margin: 0; padding: 0; }
  html, body {
    width: 777px;
    height: 1200px;
    overflow: hidden;
    background: var(--page-bg);
  }
  .canvas { position: relative; width: 777px; height: 1200px; }

  .card {
    position: absolute;
    left: 20px;
    top: 390px;
    width: 737px;
    height: 421px;
    overflow: hidden;
    background: linear-gradient(135deg, var(--card-red-light) 0%, var(--card-red) 50%, var(--card-red-dark) 100%);
    box-shadow: 0 6px 18px rgba(0,0,0,0.18);
  }

  /* Left column */
  .brand {
    position: absolute;
    left: 32px;
    top: 36px;
    display: flex;
    align-items: center;
    gap: 12px;
  }
  .brand-dot {
    width: 16px;
    height: 16px;
    border-radius: 50%;
    background: var(--benefit-green);
  }
  .brand-name {
    font-family: "Open Sans", sans-serif;
    font-weight: 400;
    font-size: 36px;
    line-height: 44px;
    color: var(--white);
  }
  .hero-frame {
    position: absolute;
    left: 32px;
    top: 104px;
    width: 296px;
    height: 190px;
    border: 5px solid var(--frame-teal);
    background: var(--white);
  }
  .hero-art {
    width: 100%;
    height: 100%;
    background: radial-gradient(circle at 50% 50%, var(--art-red) 0%, #f7b7b9 24%, var(--art-light) 58%, var(--white) 100%);
  }
  .web-row {
    position: absolute;
    left: 32px;
    top: 318px;
    display: flex;
    align-items: center;
    gap: 8px;
  }
  .web-icon { width: 20px; height: 20px; }
  .web-url {
    background: var(--white);
    border-radius: 14px;
    padding: 4px 14px;
    font-family: "Montserrat", sans-serif;
    font-weight: 700;
    font-size: 16px;
    line-height: 20px;
    letter-spacing: 0.4px;
    color: var(--url-red);
  }
  .copyright {
    position: absolute;
    left: 32px;
    top: 360px;
    font-family: "Montserrat", sans-serif;
    font-weight: 600;
    font-size: 11px;
    line-height: 16px;
    color: rgba(255,255,255,0.85);
  }

  /* Right column */
  .benefits {
    position: absolute;
    left: 368px;
    top: 36px;
    width: 337px;
  }
  .free-badge {
    display: inline-block;
    padding: 6px 22px;
    border-radius: 22px;
    background: var(--badge-red);
    border: 3px solid var(--badge-ring);
    font-family: "Montserrat", sans-serif;
    font-weight: 800;
    font-size: 20px;
    line-height: 24px;
    letter-spacing: 2px;
    color: var(--white);
  }
  .benefit-list {
    list-style: none;
    margin-top: 18px;
    display: flex;
    flex-direction: column;
    gap: 14px;
  }
  .benefit {
    display: flex;
    align-items: center;
    gap: 14px;
    height: 86px;
    padding: 0 16px;
    border-radius: 12px;
    background: var(--benefit-green);
  }
  .benefit-tick { flex: 0 0 30px; width: 30px; height: 30px; }
  .benefit-text {
    font-family: "Montserrat", sans-serif;
    font-weight: 800;
    font-size: 19px;
    line-height: 23px;
    color: var(--headline-blue);
  }
</style>
</head>
<body>
<div class="canvas">
  <section class="card">
    <div class="brand">
      <span class="brand-dot"></span>
      <span class="brand-name">StudyBrisk</span>
    </div>

    <div class="hero-frame">
      <div class="hero-art" role="img" aria-label="Illustration of two cheerful students jumping in celebration around a prize rosette"></div>
    </div>

    <div class="web-row">
      <svg class="web-icon" viewBox="0 0 20 20" aria-hidden="true">
        <circle cx="10" cy="10" r="8.5" fill="none" stroke="#fff" stroke-width="1.6"/>
        <ellipse cx="10" cy="10" rx="3.6" ry="8.5" fill="none" stroke="#fff" stroke-width="1.4"/>
        <line x1="1.5" y1="10" x2="18.5" y2="10" stroke="#fff" stroke-width="1.4"/>
      </svg>
      <span class="web-url">www.studybrisk.com</span>
    </div>

    <p class="copyright">Copyright Brisk Services, LLC 2013-20252<br>All Rights Reserved</p>

    <div class="benefits">
      <span class="free-badge">FREE</span>
      <ul class="benefit-list">
        <li class="benefit">
          <svg class="benefit-tick" viewBox="0 0 30 30" aria-hidden="true">
            <circle cx="15" cy="15" r="15" fill="#3b10e6"/>
            <path d="M8.5 15.5l4.5 4.5 8.5-9" fill="none" stroke="#fff" stroke-width="3" stroke-linecap="round" stroke-linejoin="round"/>
          </svg>
          <p class="benefit-text">Cut Study Time<br>down by up to 50%</p>
        </li>
        <li class="benefit">
          <svg class="benefit-tick" viewBox="0 0 30 30" aria-hidden="true">
            <circle cx="15" cy="15" r="15" fill="#3b10e6"/>
            <path d="M8.5 15.5l4.5 4.5 8.5-9" fill="none" stroke="#fff" stroke-width="3" stroke-linecap="round" stroke-linejoin="round"/>
          </svg>
          <p class="benefit-text">Learn a subject<br>without having to<br>go to class</p>
        </li>
        <li class="benefit">
          <svg class="benefit-tick" viewBox="0 0 30 30" aria-hidden="true">
            <circle cx="15" cy="15" r="15" fill="#3b10e6"/>
            <path d="M8.5 15.5l4.5 4.5 8.5-9" fill="none" stroke="#fff" stroke-width="3" stroke-linecap="round" stroke-linejoin="round"/>
          </svg>
          <p class="benefit-text">Memorize anything<br>quickly</p>
        </li>
      </ul>
    </div>
  </section>
</div>
</body>
</html>
```